Kelvar Systems Website

Website design for our company: Kelvar Systems.
The website should look fresh and IT focused. Please have a look at http://www.kelvarsystems.net.au/ for our current design. We want something fresh and new, professional looking, in WordPress so we can easily make changes.

Industry/Entity Type

It Company

```html
<!DOCTYPE html>
<html lang="en">
<head>
<meta charset="utf-8">
<title>Kelvar Systems</title>
<link rel="stylesheet" href="https://fonts.googleapis.com/css2?family=Open+Sans:wght@300;400;600;700&display=swap">
<style>
:root{
  --green:#0db14b;
  --green-dark:#08883a;
  --green-deep:#066b2d;
  --blue:#1b75bb;
  --blue-dark:#0b3f6e;
  --navy:#0e4a80;
  --page:#eeeeee;
  --text:#555;
  --muted:#888;
  --white:#fff;
}
*{box-sizing:border-box;margin:0;padding:0}
html,body{width:1200px;height:1138px;overflow:hidden}
body{background:var(--page);font-family:'Open Sans',sans-serif;color:var(--text);position:relative}
.abs{position:absolute}
.top-strip{left:0;top:0;width:1200px;height:7px;background:var(--green)}
.brand{left:200px;top:14px;width:124px;height:64px;border:2px solid var(--green);border-radius:4px;background:var(--white);display:flex;align-items:center;justify-content:center;gap:6px}
.brand .dot{width:14px;height:14px;border-radius:50%;background:var(--green)}
.brand span{color:var(--green);font-weight:700;font-size:13px;line-height:1.1;text-align:center}
.ip-line{right:200px;top:18px;font-size:16px;font-weight:300;color:#777}
.main-nav{left:434px;top:52px;width:566px;height:26px;display:flex;background:linear-gradient(#1f6db0,var(--blue-dark))}
.main-nav a{flex:auto;color:var(--white);font-size:12.5px;text-decoration:none;display:flex;align-items:center;justify-content:center;border-right:1px solid rgba(255,255,255,.15)}
.main-nav a.active{background:linear-gradient(#17c35a,var(--green-dark))}
.slider{left:234px;top:103px;width:480px;height:305px;border:3px solid var(--white);box-shadow:0 1px 4px rgba(0,0,0,.25);background:linear-gradient(120deg,#c9c3b4,#9fa3a3 45%,#d98c52 80%,#e9e2d8)}
.arrow{top:224px}
.caption{left:236px;top:168px;width:190px;height:160px;background:rgba(40,40,40,.72);color:var(--white);text-align:center;padding:14px 10px}
.caption h2{font-weight:300;font-size:21px;line-height:1.15}
.caption p{font-size:11.5px;line-height:1.35;margin-top:6px;color:#ddd}
.btn{display:flex;align-items:center;justify-content:center;color:var(--white);font-weight:700;font-size:10px;text-transform:uppercase;border-radius:2px}
.btn-green{background:linear-gradient(#17c35a,var(--green-deep));border:1px solid #0a5a27}
.btn-blue{background:linear-gradient(#2c78b8,var(--blue-dark))}
.caption .btn{position:absolute;left:46px;top:114px;width:96px;height:32px}
.remote{left:780px;top:102px;width:220px;height:90px;background:#f3f3f3;border:1px solid #ddd;padding:6px 8px}
.remote h3{color:var(--blue);font-weight:400;font-size:20px;line-height:1.1}
.remote p{font-size:9px;color:#333;margin-top:2px}
.remote .field{position:absolute;left:8px;top:54px;width:100px;height:22px;background:var(--white);border:1px solid #ccc;font-size:9px;color:#aaa;padding:4px 6px}
.remote .btn{position:absolute;left:122px;top:54px;width:90px;height:22px;font-size:9.5px}
.testi-title{left:788px;top:204px;color:var(--green);font-size:20px}
.testimonials{left:780px;top:232px;width:220px}
.testimonial{display:flex;height:49px;background:var(--green);border-bottom:1px solid #0a9b40}
.testimonial:nth-child(2){background:#14c35a}
.testimonial .date{width:36px;background:rgba(0,0,0,.12);color:var(--white);font-size:8px;display:flex;align-items:center;justify-content:center}
.testimonial .body{flex:1;padding:3px 5px;color:var(--white);font-size:9px;line-height:1.25}
.testimonial .name{color:#064d22;font-size:11px}
.testimonial .more{color:#0a5a27;text-decoration:underline}
.testi-btn{left:846px;top:389px;width:89px;height:19px;font-size:9px}
.floor{left:0;top:552px;width:1200px;height:48px;background:linear-gradient(#d8d8d8,#f2f2f2)}
.feature-art{top:414px;height:174px;width:200px}
.feature{top:612px;width:230px;text-align:center}
.feature h4{color:var(--blue);font-weight:400;font-size:12.5px;line-height:1.15}
.feature p{font-size:10px;line-height:1.4;color:#777;margin-top:3px}
.feature-btn{top:708px;width:97px;height:31px}
.partners{left:200px;top:758px;width:800px;height:131px;background:var(--white)}
.partners h3{position:absolute;left:8px;top:5px;color:var(--green);font-weight:400;font-size:21px}
.badge{position:absolute;top:48px;height:62px;border-radius:6px;background:#dfe6ee}
.welcome{left:200px;top:914px;width:650px}
.welcome h2{color:var(--green);font-weight:400;font-size:22px;line-height:1.2}
.welcome p{font-size:9.5px;line-height:1.55;color:#444}
.brand-small{left:876px;top:938px;width:124px;height:63px}
.footer{left:0;top:1044px;width:1200px;height:94px;background:var(--green);color:var(--white)}
.footer-links{position:absolute;left:201px;top:16px;font-size:12px;line-height:1.45}
.footer-links .rights{color:#1b75bb;font-size:10px}
.contact h5{position:absolute;left:498px;top:10px;font-weight:400;font-size:13px}
.contact .in{position:absolute;height:19px;width:98px;background:var(--white);border:1px solid #ccc;color:#bbb;font-size:9px;padding:3px 5px}
.contact .btn{position:absolute;left:626px;top:54px;width:58px;height:19px}
.footer ul{position:absolute;left:810px;top:10px;list-style:none;font-size:10px;line-height:1.65;font-weight:600}
.footer li::before{content:"• "}
</style>
</head>
<body>
<div class="abs top-strip"></div>

<header>
  <div class="abs brand"><div class="dot"></div><span>Kelvar Systems</span></div>
  <p class="abs ip-line">Your IP address is 203.0.113.42 which resolves to host-203-0-113-42.northlinknet.com</p>
  <nav class="abs main-nav">
    <a class="active">Home</a><a>Clients</a><a>Services</a><a>Supports</a><a>Testimonials</a><a>Contact Us</a><a>About Us</a>
  </nav>
</header>

<section class="hero">
  <div class="abs slider" role="img" aria-label="Photo of hands typing on a laptop keyboard in an office"></div>
  <svg class="abs arrow" style="left:200px" width="20" height="38" viewBox="0 0 20 38"><polygon points="20,0 0,19 20,38" fill="#0db14b"/></svg>
  <svg class="abs arrow" style="left:727px" width="20" height="38" viewBox="0 0 20 38"><polygon points="0,0 20,19 0,38" fill="#0db14b"/></svg>
  <div class="abs caption">
    <h2>Aliquam elit arcu, iaculis se</h2>
    <p>mollis a, hendrerit a odio. Nam placerat mi id semper gravida. Nunc vel molestie ipsum, quis tincidunt</p>
    <a class="btn btn-green">View More</a>
  </div>
</section>

<aside>
  <div class="abs remote">
    <h3>REMOTE SUPPORT</h3>
    <p>Enter your 6-digit code</p>
    <div class="field">Code</div>
    <a class="btn btn-blue">Connect Now</a>
  </div>
  <h3 class="abs testi-title">LAST TESTIMONIES</h3>
  <div class="abs testimonials">
    <div class="testimonial"><div class="date">JAN-28</div><div class="body"><div class="name">JOHN DOE</div>Adipiscing elit. Etiam sed sodales neque vitae orci pharetra rhoncus. <span class="more">Read more</span></div></div>
    <div class="testimonial"><div class="date">JAN-28</div><div class="body"><div class="name">JOHN DOE</div>Adipiscing elit. Etiam sed sodales neque vitae orci pharetra rhoncus. <span class="more">Read more</span></div></div>
    <div class="testimonial"><div class="date">JAN-28</div><div class="body"><div class="name">JOHN DOE</div>Adipiscing elit. Etiam sed sodales neque vitae orci pharetra rhoncus. <span class="more">Read more</span></div></div>
  </div>
  <a class="abs btn btn-green testi-btn">View More</a>
</aside>

<section class="features">
  <div class="abs floor"></div>
  <div class="abs feature-art" style="left:234px;background:linear-gradient(#4a4f57,#1d2024)" role="img" aria-label="Illustration of a row of server racks"></div>
  <div class="abs feature-art" style="left:500px;background:linear-gradient(#9aa6b2,#3f6b9c)" role="img" aria-label="Illustration of gears above a laptop"></div>
  <div class="abs feature-art" style="left:780px;width:170px;border-radius:50%;height:170px;background:radial-gradient(#f4f4f4,#c9c9d9)" role="img" aria-label="Illustration of a sphere covered in consulting keywords"></div>

  <div class="abs feature" style="left:219px"><h4>LOREM IPSUM DOLOR SIT AMET, CONSECTETUR ADIPISCING ELIT.</h4><p>Morbi risus risus, imperdiet at ligula a, vulputate ultricies justo. Curabitur porta dolor ac congue venenatis. Vivamus adipiscing lorem augue, at viverra ligula gravida sed.</p></div>
  <div class="abs feature" style="left:485px"><h4>LOREM IPSUM DOLOR SIT AMET, CONSECTETUR ADIPISCING ELIT.</h4><p>Morbi risus risus, imperdiet at ligula a, vulputate ultricies justo. Curabitur porta dolor ac congue venenatis. Vivamus adipiscing lorem augue, at viverra ligula gravida sed.</p></div>
  <div class="abs feature" style="left:752px"><h4>LOREM IPSUM DOLOR SIT AMET, CONSECTETUR ADIPISCING ELIT.</h4><p>Morbi risus risus, imperdiet at ligula a, vulputate ultricies justo. Curabitur porta dolor ac congue venenatis. Vivamus adipiscing lorem augue, at viverra ligula gravida sed.</p></div>

  <a class="abs btn btn-blue feature-btn" style="left:285px">View More</a>
  <a class="abs btn btn-blue feature-btn" style="left:552px">View More</a>
  <a class="abs btn btn-blue feature-btn" style="left:819px">View More</a>
</section>

<section class="abs partners">
  <h3>OUR PARTNERS</h3>
  <div class="badge" style="left:36px;width:116px"></div>
  <div class="badge" style="left:186px;width:80px"></div>
  <div class="badge" style="left:298px;width:120px"></div>
  <div class="badge" style="left:448px;width:104px"></div>
  <div class="badge" style="left:584px;width:190px"></div>
</section>

<section class="abs welcome">
  <h2>Welcome to Kelvar Systems</h2>
  <p>Kelvar Systems is an Adelaide based company with a single objective - to excel in the support and service of all computer and IT needs.<br>
  We provide a high level of consulting services using the most experienced engineers at a reasonable and fair price. We believe in using a Business Value approach to every aspect of computer consulting to provide our clients with the most cost effective solutions.<br>
  We strongly believe that we are in business with our clients. Each thing we do must be measured against our clients' business objectives. At the end of the day our client's success is our success.</p>
</section>
<div class="abs brand brand-small"><div class="dot"></div><span>Kelvar Systems</span></div>

<footer class="abs footer">
  <div class="footer-links">Home &nbsp;|&nbsp; Clients &nbsp;|&nbsp; Services &nbsp;|&nbsp; Supports<br>Testimonials &nbsp;|&nbsp; Contact Us &nbsp;|&nbsp; About Us<br><span class="rights">All rights reserved</span></div>
  <div class="contact">
    <h5>CONTACT</h5>
    <div class="in" style="left:496px;top:29px">Name</div>
    <div class="in" style="left:606px;top:29px">Email</div>
    <div class="in" style="left:496px;top:54px">Phone</div>
    <a class="btn btn-blue">Send</a>
  </div>
  <ul>
    <li>Lorem ipsum dolor sit amet</li>
    <li>Consectetur adipiscing elit.</li>
    <li>Etiam egestas mi in volutpat tincidunt.</li>
    <li>Etiam fringilla enim eu lorem mattis</li>
  </ul>
</footer>
</body>
</html>
```